Upmarket building and construction company needs signage

Our building company R Brent Construction, needs signage to put up on the side of our vehicle trailers and on site fencing. We are a building company that specialises in residential construction and carpentry .

I will attach our logo and some inspirational pics for site fencing as well as what our trailer looks like .
Other details i would like on the sign are our
( email) rbrentconstruction@mailbox-example.net
(mobile ) 0493 518 264
(website ) rbrentconstruction. example.net

Target Market(s)

Home owners looking for a reliable local builder who produces good quality work. I have attached some inspirational pics.

Industry/Entity Type

Building and Construction

Colors

Designer to choose colors to be used in the design.

Requirements
Must have
• Our logo, contact information
Nice to have
• We would like the design to have elements of being Elegant, Serious, Modern, Professional, Masculine, Conservative and Upmarket.

```html
<!DOCTYPE html>
<html lang="en">
<head>
<meta charset="UTF-8">
<title>R Brent Construction – Trailer Signage</title>
<link href="https://fonts.googleapis.com/css2?family=Montserrat:wght@400;500&display=swap" rel="stylesheet">
<style>
  :root {
    --backdrop: #e6e6e6;
    --sign-grey: #71716f;
    --house-grey: #818181;
    --ink-white: #ffffff;
  }
  * { margin: 0; padding: 0; box-sizing: border-box; }
  html, body {
    width: 1200px;
    height: 719px;
    overflow: hidden;
    background: var(--backdrop);
    font-family: "Montserrat", Arial, sans-serif;
  }
  .sign {
    position: absolute;
    left: 120px;
    top: 119px;
    width: 960px;
    height: 480px;
    background: var(--sign-grey);
    overflow: hidden;
    color: var(--ink-white);
  }
  .house-illustration {
    position: absolute;
    left: 338px;
    top: 300px;
    width: 622px;
    height: 180px;
    background: linear-gradient(180deg, rgba(129,129,129,0) 0%, var(--house-grey) 35%, var(--house-grey) 100%);
  }
  .brand-name {
    position: absolute;
    left: 82px;
    top: 203px;
    width: 270px;
    font-weight: 400;
    color: var(--ink-white);
    line-height: 1;
  }
  .brand-name .brand-primary {
    display: block;
    font-size: 56px;
    letter-spacing: 1px;
  }
  .brand-name .brand-secondary {
    display: block;
    margin-top: 14px;
    font-size: 26px;
    letter-spacing: 3.4px;
  }
  .brand-name .brand-tagline {
    display: block;
    margin-top: 12px;
    font-size: 17px;
    letter-spacing: 1.6px;
  }
  .contact {
    position: absolute;
    right: 49px;
    top: 183px;
    text-align: right;
    font-weight: 500;
    font-style: normal;
    line-height: 1;
  }
  .contact .phone {
    display: block;
    font-size: 46px;
    letter-spacing: 0.5px;
  }
  .contact .email {
    display: block;
    margin-top: 10px;
    font-size: 21px;
  }
  .contact .website {
    display: block;
    margin-top: 6px;
    font-size: 26px;
  }
</style>
</head>
<body>
  <section class="sign">
    <div class="house-illustration" role="img" aria-label="Line illustration of a modern single-storey house with a double garage"></div>

    <h1 class="brand-name">
      <span class="brand-primary">R BRENT</span>
      <span class="brand-secondary">CONSTRUCTION</span>
      <span class="brand-tagline">BUILDING AND CARPENTRY</span>
    </h1>

    <address class="contact">
      <span class="phone">+61 493 518 264</span>
      <span class="email">rbrentconstruction@mailbox-example.net</span>
      <span class="website">rbrentconstruction. example.net</span>
    </address>
  </section>
</body>
</html>
```